2024 Harwick Patrol Deputy's Statute Handbook

Cover, spine and back cover for our annual law manual. The overall size of the cover is 18.82 x 11 (with the .25 inch bleed it is 19.32 x 11.5) and the spine is 1.82 x 11 plus (1.82 x 11.5 with the bleed).
The book comes with a motor vehicle companion guide which will be 5" X 7" with spiral binding. The companion guide will have the same design with a slight twist related to motor vehicle law.

```html
<!DOCTYPE html>
<html lang="en">
<head>
<meta charset="utf-8">
<title>Harwick Patrol Deputy's Statute Handbook 2024 – Cover</title>
<link rel="stylesheet" href="https://fonts.googleapis.com/css2?family=Bungee&family=Oswald:wght@500;600;700&family=Poppins:wght@400&display=swap">
<style>
  :root {
    --navy-deep: #070b14;
    --navy: #141d33;
    --navy-mid: #1f2b48;
    --teal: #2aa9aa;
    --teal-light: #7fe0dc;
    --gold: #c99a22;
    --gold-light: #f0cf6a;
    --gold-dark: #7a5a0e;
    --silver: #d9dde3;
    --white: #ffffff;
    --flag-red: #7a2a30;
  }
  * { margin: 0; padding: 0; box-sizing: border-box; }
  html, body { width: 1200px; height: 714px; overflow: hidden; background: var(--navy-deep); }
  .cover { position: relative; width: 1200px; height: 714px; overflow: hidden; }

  .cover-photo {
    position: absolute; inset: 0;
    background:
      radial-gradient(ellipse 260px 200px at 1110px 640px, rgba(122,42,48,.55), transparent 70%),
      radial-gradient(ellipse 300px 260px at 960px 230px, var(--navy-mid), transparent 75%),
      radial-gradient(ellipse 280px 360px at 220px 300px, #1b2233, transparent 75%),
      linear-gradient(100deg, var(--navy-deep) 0%, var(--navy) 45%, var(--navy-deep) 52%, var(--navy) 70%, #18223b 100%);
  }
  .handcuffs-photo {
    position: absolute; left: 610px; top: 350px; width: 260px; height: 230px;
    background: radial-gradient(ellipse at 50% 50%, rgba(217,221,227,.55) 0%, rgba(150,158,170,.25) 45%, transparent 72%);
  }

  .back-blurb {
    position: absolute; left: 55px; top: 189px; width: 452px;
    font-family: "Poppins", sans-serif; font-size: 9.9px; line-height: 12.35px;
    color: var(--white); text-align: justify;
  }
  .back-blurb p + p { margin-top: 12.3px; }

  .isbn-box { position: absolute; left: 359px; top: 594px; width: 148px; height: 74px; background: var(--white); }

  .title-art { position: absolute; inset: 0; }
  .title-art text { font-family: "Bungee", sans-serif; }
  .title-art .condensed { font-family: "Oswald", sans-serif; font-weight: 700; }
  .title-art .condensed-mid { font-family: "Oswald", sans-serif; font-weight: 600; }
  .brand-name { font-family: "Oswald", sans-serif; font-weight: 600; fill: var(--gold-light); }
</style>
</head>
<body>
<main class="cover">
  <div class="cover-photo" role="img" aria-label="Dark photograph of a police officer's tactical uniform and vest with a faded American flag"></div>
  <div class="handcuffs-photo" role="img" aria-label="Photograph of a pair of chrome handcuffs"></div>

  <section class="back-blurb">
    <p>Lorem ipsum dolor sit amet, consectetur adipiscing elit, sed do eiusmod tempor incididunt ut labore et dolore magna aliqua. Ut enim ad minim veniam, quis nostrud exercitation ullamco laboris nisi ut aliquip ex ea commodo consequat. Duis aute irure dolor in reprehenderit in voluptate velit esse cillum dolore eu fugiat nulla pariatur. Excepteur sint occaecat cupidatat non proident, sunt in culpa qui officia deserunt mollit anim id est laborum.</p>
    <p>Sed ut perspiciatis unde omnis iste natus error sit voluptatem accusantium doloremque laudantium, totam rem aperiam, eaque ipsa quae ab illo inventore veritatis et quasi architecto beatae vitae dicta sunt explicabo. Nemo enim ipsam voluptatem quia voluptas sit aspernatur aut odit aut fugit, sed quia consequuntur magni dolores eos qui ratione voluptatem sequi nesciunt. Neque porro quisquam est, qui dolorem ipsum quia dolor sit amet, consectetur, adipisci velit, sed quia non numquam eius modi tempora incidunt ut labore et dolore magnam aliquam quaerat voluptatem. Ut enim ad minima veniam, quis nostrum exercitationem ullam corporis suscipit laboriosam, nisi ut aliquid ex ea commodi consequatur? Quis autem vel eum iure reprehenderit qui in ea voluptate velit esse quam nihil molestiae consequatur, vel illum qui dolorem eum fugiat quo voluptas nulla pariatur</p>
    <p>At vero eos et accusamus et iusto odio dignissimos ducimus qui blanditiis praesentium voluptatum deleniti atque corrupti quos dolores et quas molestias excepturi sint occaecati cupiditate non provident, similique sunt in culpa qui officia deserunt mollitia animi, id est laborum et dolorum fuga. Et harum quidem rerum facilis est et expedita distinctio. Nam libero tempore, cum soluta nobis est eligendi optio cumque nihil impedit quo minus id quod maxime placeat facere possimus, omnis voluptas assumenda est, omnis dolor repellendus. Temporibus autem quibusdam et aut officiis debitis aut rerum necessitatibus saepe eveniet ut et voluptates repudiandae sint et molestiae non recusandae. Itaque earum rerum hic tenetur a sapiente delectus, ut aut reiciendis voluptatibus maiores alias consequatur aut perferendis doloribus asperiores repellat.</p>
  </section>

  <div class="isbn-box"></div>

  <svg class="title-art" width="1200" height="714" viewBox="0 0 1200 714">
    <defs>
      <linearGradient id="gold-fill" x1="0" y1="0" x2="0" y2="1">
        <stop offset="0" stop-color="var(--gold-light)"/>
        <stop offset=".5" stop-color="var(--gold)"/>
        <stop offset="1" stop-color="var(--gold-dark)"/>
      </linearGradient>
      <linearGradient id="teal-fill" x1="0" y1="0" x2="0" y2="1">
        <stop offset="0" stop-color="var(--teal-light)"/>
        <stop offset=".55" stop-color="var(--teal)"/>
        <stop offset="1" stop-color="#13605f"/>
      </linearGradient>
      <linearGradient id="chrome-fill" x1="0" y1="0" x2="0" y2="1">
        <stop offset="0" stop-color="var(--white)"/>
        <stop offset=".55" stop-color="var(--silver)"/>
        <stop offset="1" stop-color="#8d939c"/>
      </linearGradient>
    </defs>

    <!-- Back cover title -->
    <g class="back-title" stroke="#0b1220" stroke-width="1.5" paint-order="stroke">
      <text x="112" y="90" font-size="30" textLength="338" lengthAdjust="spacingAndGlyphs" fill="url(#teal-fill)">PATROL DEPUTY'S</text>
      <text x="60" y="141" font-size="44" textLength="435" lengthAdjust="spacingAndGlyphs" fill="url(#gold-fill)">STATUTE HANDBOOK</text>
      <text x="205" y="175" font-size="32" textLength="145" lengthAdjust="spacing" fill="url(#teal-fill)">2024</text>
    </g>

    <!-- Spine -->
    <g class="spine-brand">
      <circle cx="600" cy="44" r="11" fill="var(--gold)"/>
      <text class="brand-name" x="600" y="69" font-size="7.5" text-anchor="middle">CALDER TRAINING</text>
    </g>
    <g class="spine-title" stroke="#0b1220" stroke-width="1.2" paint-order="stroke">
      <text transform="translate(563,198) rotate(90)" font-size="21" textLength="216" lengthAdjust="spacingAndGlyphs" fill="url(#teal-fill)">PATROL DEPUTY'S</text>
      <text transform="translate(590,171) rotate(90)" font-size="32" textLength="273" lengthAdjust="spacingAndGlyphs" fill="url(#gold-fill)">STATUTE HANDBOOK</text>
      <text transform="translate(623,261) rotate(90)" font-size="18" textLength="93" lengthAdjust="spacing" fill="url(#teal-fill)">2024</text>
    </g>
    <text class="condensed-mid spine-author" transform="translate(592,480) rotate(90)" font-size="17" textLength="180" lengthAdjust="spacingAndGlyphs" fill="url(#chrome-fill)">DORIAN K. WHITLOCK ESQ.</text>

    <!-- Front cover -->
    <text class="condensed-mid front-author" x="780" y="70" font-size="27" textLength="315" lengthAdjust="spacingAndGlyphs" fill="url(#chrome-fill)">DORIAN K. WHITLOCK ESQ.</text>
    <g class="front-title" stroke="#0b1220" stroke-width="2" paint-order="stroke">
      <text x="770" y="113" font-size="33" textLength="315" lengthAdjust="spacingAndGlyphs" fill="url(#teal-fill)">PATROL DEPUTY'S</text>
      <text x="762" y="205" font-size="86" textLength="315" lengthAdjust="spacingAndGlyphs" fill="url(#gold-fill)">STATUTE</text>
      <text x="762" y="285" font-size="52" textLength="323" lengthAdjust="spacingAndGlyphs" fill="url(#gold-fill)">HANDBOOK</text>
      <text x="762" y="345" font-size="54" textLength="323" lengthAdjust="spacing" fill="url(#teal-fill)">2024</text>
    </g>

    <g class="front-brand">
      <circle cx="922" cy="430" r="14" fill="var(--gold)"/>
      <text class="brand-name" x="922" y="462" font-size="13" text-anchor="middle">CALDER</text>
      <text class="brand-name" x="922" y="477" font-size="13" text-anchor="middle">TRAINING</text>
    </g>

    <g class="front-subtitle" stroke="#05080f" stroke-width="2" paint-order="stroke">
      <text class="condensed" x="791" y="558" font-size="46" textLength="262" lengthAdjust="spacingAndGlyphs" fill="url(#chrome-fill)">HARWICK</text>
      <text class="condensed-mid" x="831" y="586" font-size="30" textLength="183" lengthAdjust="spacingAndGlyphs" fill="url(#chrome-fill)">PATROL DEPUTY'S</text>
      <text class="condensed-mid" x="870" y="630" font-size="21" textLength="108" lengthAdjust="spacing" fill="var(--white)">GUIDE TO</text>
      <text class="condensed-mid" x="701" y="658" font-size="16" textLength="445" lengthAdjust="spacingAndGlyphs" fill="var(--white)">CRIMINAL PROCEDURE <tspan fill="var(--gold-light)">•</tspan> STATUTORY LAW <tspan fill="var(--gold-light)">•</tspan> MOTOR VEHICLE LAW <tspan fill="var(--gold-light)">•</tspan> JUVENILE LAW</text>
    </g>
  </svg>
</main>
</body>
</html>
```